Varden Homes needs a stationery design

I need a stationary design for my new custom home building company. Our company deals with very high end and luxurious homes so i need a stationary design that shows strength, elegance, and trust.
The final version should be trendy, clean... only 2 colours (green + grey/black) and professional.
#1: Business Cards (design on 2 sides)
#2: Letterhead (word format)
#3: Cover Page and back cover for proposals
#4: Envelopes,
#5: Thank You card,
#6: Presentation Folder
Logo is attached. Logo can be reversed out (will attach once available). Logo can be stacked or horizontal (provided as horizontal).
The business cards need to be two sided with the company logo and website on the front (www.vardenhomes-example.com and contact info on the back.
The contact info can be made up temporarily and once the final design is chosen, i will provide you with all the correct contact information during the revision stage.
id like to see examples with black, white, blue, red, purple. (You should not try to use all these in one design)
I have attached my company's logo in 3 different colours and a few sample business cards that i found on the internet. I would like to see unique designs though, don't try to imitate the examples
Updates
Dear designers,
I have also attached the .eps and ai files for the 3 different coloured logos.
Please notify me if you need anything else to complete your work
Best Regards,
Varden

```html
<!DOCTYPE html>
<html lang="en">
<head>
<meta charset="utf-8">
<title>Varden Homes – Business Card Concepts</title>
<link rel="stylesheet" href="https://fonts.googleapis.com/css2?family=Open+Sans:wght@400;600;700&display=swap">
<style>
  :root {
    --board: #b3b3b3;
    --navy: #050b2e;
    --slate: #4b4b4b;
    --card: #cfcfcf;
    --muted: #5a5a5a;
    --ink: #111;
  }
  * { box-sizing: border-box; margin: 0; padding: 0; }
  html, body { width: 1200px; height: 1000px; overflow: hidden; }
  body {
    background: var(--board);
    font-family: "Open Sans", Arial, sans-serif;
    color: var(--ink);
    position: relative;
  }
  .caption {
    position: absolute;
    font-size: 10px;
    letter-spacing: 0.1px;
    text-transform: uppercase;
    white-space: nowrap;
  }
  .caption--two-sided { left: 0; width: 1254px; text-align: center; top: 128px; }
  .caption--one-sided { left: 0; width: 1208px; text-align: center; top: 877px; }
  .caption--note { right: 34px; top: 964px; }
  .caption--transparent { left: 997px; top: 683px; }
  .callout-line {
    position: absolute; left: 820px; top: 688px;
    width: 167px; height: 1px; background: #444;
  }

  .card {
    position: absolute;
    background: var(--card);
    box-shadow: 6px 7px 8px rgba(0,0,0,0.45);
    overflow: hidden;
  }
  .card--front { left: 137px; top: 167px; width: 469px; height: 268px; }
  .card--back  { left: 642px; top: 167px; width: 469px; height: 268px; }
  .card--clear { left: 363px; top: 574px; width: 465px; height: 266px; background: transparent; }

  .card__clear-bg { position: absolute; inset: 0; width: 100%; height: 100%; }
  .card__top-band {
    position: absolute; left: 0; top: 0; width: 100%; height: 22px;
    background: var(--navy);
    border-bottom: 5px solid var(--slate);
    height: 27px;
  }
  .card__bottom-band { position: absolute; left: 0; bottom: 0; width: 100%; height: 22px; }

  .wordmark {
    position: absolute;
    display: flex; align-items: center; gap: 10px;
    color: var(--navy);
    font-weight: 700;
    text-transform: uppercase;
    white-space: nowrap;
    line-height: 1;
  }
  .wordmark__square { width: 14px; height: 14px; background: var(--slate); flex: none; }
  .wordmark--large { left: 0; width: 100%; justify-content: center; top: 104px; font-size: 34px; letter-spacing: 2px; }
  .wordmark--small { left: 14px; top: 70px; font-size: 26px; letter-spacing: 1px; }

  .website {
    position: absolute; left: 0; width: 100%; text-align: center;
    color: var(--navy); font-weight: 600; white-space: nowrap;
  }
  .card--front .website { top: 181px; font-size: 13px; letter-spacing: 3.2px; }
  .card--back .website  { top: 228px; font-size: 12px; letter-spacing: 2.6px; left: 20px; }
  .card--clear .website { top: 228px; font-size: 12px; letter-spacing: 2.6px; left: 20px; }

  .address { position: absolute; font-size: 11px; color: var(--navy); white-space: nowrap; }
  .card--back .address  { left: 286px; top: 82px; }
  .card--clear .address { left: 283px; top: 82px; }

  .person { position: absolute; width: 160px; text-align: center; }
  .card--back .person  { left: 31px; top: 144px; }
  .card--clear .person { left: 30px; top: 142px; }
  .person__name { font-size: 15px; color: var(--navy); letter-spacing: 1px; line-height: 1.2; word-spacing: 4px; }
  .person__role { font-size: 11px; color: var(--muted); text-transform: uppercase; line-height: 1.3; }

  .contact { position: absolute; border-collapse: collapse; font-size: 10.5px; color: var(--navy); text-transform: uppercase; }
  .contact td { padding: 0; height: 17.5px; white-space: nowrap; }
  .contact .contact__value { font-size: 9.5px; text-transform: none; }
  .card--back .contact  { left: 229px; top: 136px; }
  .card--back .contact td:first-child { width: 134px; }
  .card--clear .contact { left: 227px; top: 135px; }
  .card--clear .contact td:first-child { width: 132px; }
</style>
</head>
<body>
  <p class="caption caption--two-sided">Two-sided business card</p>

  <section class="card card--front" aria-label="Business card front">
    <div class="card__top-band"></div>
    <div class="wordmark wordmark--large"><span class="wordmark__square"></span>Varden Homes</div>
    <p class="website">www.vardenhomes-example.com</p>
    <svg class="card__bottom-band" viewBox="0 0 469 22" preserveAspectRatio="none" aria-hidden="true">
      <polygon points="0,0 154,0 132,22 0,22" fill="var(--slate)"/>
      <polygon points="154,0 160,0 138,22 132,22" fill="#eaeaea"/>
      <polygon points="160,0 469,0 469,22 143,22" fill="var(--navy)"/>
    </svg>
  </section>

  <section class="card card--back" aria-label="Business card back">
    <div class="card__top-band"></div>
    <div class="wordmark wordmark--small"><span class="wordmark__square"></span>Varden Homes</div>
    <p class="address">Business Address Here</p>
    <div class="person">
      <p class="person__name">JOHN DOE</p>
      <p class="person__role">Position</p>
    </div>
    <table class="contact">
      <tr><td>Phone No.:</td><td class="contact__value">xxx - xxx - xxxx</td></tr>
      <tr><td>Fax No.:</td><td class="contact__value">xxx - xxx - xxxx</td></tr>
      <tr><td>Email Address:</td><td class="contact__value">xxx - xxx - xxxx</td></tr>
    </table>
    <p class="website">www.vardenhomes-example.com</p>
    <svg class="card__bottom-band" viewBox="0 0 469 22" preserveAspectRatio="none" aria-hidden="true">
      <polygon points="0,0 154,0 132,22 0,22" fill="var(--slate)"/>
      <polygon points="154,0 160,0 138,22 132,22" fill="#eaeaea"/>
      <polygon points="160,0 469,0 469,22 143,22" fill="var(--navy)"/>
    </svg>
  </section>

  <section class="card card--clear" aria-label="Transparent business card">
    <svg class="card__clear-bg" viewBox="0 0 465 266" preserveAspectRatio="none" aria-hidden="true">
      <defs>
        <linearGradient id="clear-sheen" x1="0" y1="0" x2="1" y2="0">
          <stop offset="0" stop-color="#fafafa"/>
          <stop offset="0.4" stop-color="#c4c4c4"/>
          <stop offset="1" stop-color="#c8c8c8"/>
        </linearGradient>
      </defs>
      <rect width="465" height="266" fill="url(#clear-sheen)"/>
      <path d="M200,20 C160,90 170,190 210,266 L465,266 L465,20 Z" fill="#d4d4d4"/>
    </svg>
    <div class="card__top-band"></div>
    <div class="wordmark wordmark--small"><span class="wordmark__square"></span>Varden Homes</div>
    <p class="address">Business Address Here</p>
    <div class="person">
      <p class="person__name">JOHN DOE</p>
      <p class="person__role">Position</p>
    </div>
    <table class="contact">
      <tr><td>Phone No.:</td><td class="contact__value">xxx - xxx - xxxx</td></tr>
      <tr><td>Fax No.:</td><td class="contact__value">xxx - xxx - xxxx</td></tr>
      <tr><td>Email Address:</td><td class="contact__value">xxx - xxx - xxxx</td></tr>
    </table>
    <p class="website">www.vardenhomes-example.com</p>
    <svg class="card__bottom-band" viewBox="0 0 465 22" preserveAspectRatio="none" aria-hidden="true">
      <polygon points="0,0 152,0 130,22 0,22" fill="var(--slate)"/>
      <polygon points="152,0 158,0 136,22 130,22" fill="#eaeaea"/>
      <polygon points="158,0 465,0 465,22 141,22" fill="var(--navy)"/>
    </svg>
  </section>

  <div class="callout-line"></div>
  <p class="caption caption--transparent">Transparent</p>
  <p class="caption caption--one-sided">One-sided transparent business card</p>
  <p class="caption caption--note">Color designs can be changed if desired</p>
</body>
</html>
```